Healthy Supplement featuring Moringa products

Need 3 business card options for our reps to order from Cardloom. Our reps will be ordering from Cardloom once we upload them. Attached is our current designs to show what info needs to be on the cards. Our website is www.tkvitality.com
The business cards will be a template for our reps to order from. Most of our reps are Asian & Hispanic. Please look at our website so you can see who we are to get the look and feel what we need.
Target Market(s)
Adults 30 on up. Health oriented people.
Industry/Entity Type
Health And Wellness
Contact Information for Business Card
Name
Title
Phone
Logo
www.tkvitality.com/my/username
Font styles to use
Requirements
Must have
- Please match our website look and colors. A moringa leaf is nice, but am open to something different.
Nice to have
- Healthy looking and warm, not super cold or too modern.
Should not have
- No harsh colors please.

```html
<!DOCTYPE html>
<html lang="en">
<head>
<meta charset="utf-8">
<title>TK Vitality – Business Card</title>
<link href="https://fonts.googleapis.com/css2?family=Source+Sans+3:wght@400;600&display=swap" rel="stylesheet">
<style>
  :root {
    --forest: #1c5a28;
    --forest-leaf: #3f7246;
    --mist: #eff6ef;
    --sage: #dde2c6;
    --leaf-green: #6aab3c;
    --white: #ffffff;
  }
  html, body {
    margin: 0;
    padding: 0;
    width: 1200px;
    height: 433px;
    overflow: hidden;
    background: var(--white);
    font-family: "Source Sans 3", sans-serif;
  }
  .canvas {
    position: relative;
    width: 1200px;
    height: 433px;
  }
  .card {
    position: absolute;
    top: 53px;
    width: 567px;
    height: 367px;
    overflow: hidden;
  }
  .card--front { left: 0; background: var(--forest); }
  .card--back  { left: 627px; background: var(--mist); }

  .card__pattern {
    position: absolute;
    inset: 0;
  }
  .card--front .card__pattern {
    background: radial-gradient(circle at 50% 50%, var(--forest) 35%, #245f2f 70%, var(--forest) 100%);
  }
  .card--back .card__pattern {
    background: radial-gradient(circle at 50% 50%, var(--mist) 30%, #e7eddc 70%, var(--mist) 100%);
  }

  .medallion {
    position: absolute;
    left: 164px;
    top: 64px;
    width: 240px;
    height: 240px;
    border-radius: 50%;
    display: flex;
    flex-direction: column;
    align-items: center;
    justify-content: center;
  }
  .card--front .medallion { background: var(--mist); }
  .card--back .medallion { background: var(--forest); left: 163px; }

  .brand {
    display: flex;
    align-items: center;
    gap: 8px;
    color: var(--leaf-green);
    font-weight: 600;
    font-size: 30px;
    letter-spacing: 2px;
  }
  .brand__dot {
    width: 16px;
    height: 16px;
    border-radius: 50%;
    background: var(--leaf-green);
  }

  .identity {
    text-align: center;
    line-height: 1;
    margin-top: -8px;
  }
  .identity__word {
    color: var(--leaf-green);
    font-size: 31px;
    letter-spacing: -0.5px;
  }
  .identity__name {
    color: var(--white);
    font-size: 28px;
    letter-spacing: -1px;
    margin-top: 10px;
  }
  .identity__title {
    color: var(--white);
    font-size: 28px;
    letter-spacing: -1px;
    margin-top: 2px;
  }
  .contacts {
    list-style: none;
    margin: 22px 0 0 0;
    padding: 0 0 0 0;
    width: 140px;
  }
  .contacts__item {
    display: flex;
    align-items: center;
    gap: 9px;
    color: var(--white);
    font-size: 13.5px;
    letter-spacing: -0.6px;
    height: 24.5px;
  }
  .contacts__icon {
    width: 14px;
    height: 14px;
    flex: none;
    fill: var(--white);
  }
</style>
</head>
<body>
<main class="canvas">

  <section class="card card--front">
    <div class="card__pattern" role="img" aria-label="Scattered outline leaf pattern in muted green"></div>
    <div class="medallion">
      <div class="brand"><span class="brand__dot"></span>TK VITALITY</div>
    </div>
  </section>

  <section class="card card--back">
    <div class="card__pattern" role="img" aria-label="Pale sage pattern of leaves and sprigs"></div>
    <div class="medallion">
      <div class="identity">
        <div class="identity__word">VITALITY</div>
        <div class="identity__name">YOUR NAME</div>
        <div class="identity__title">Title</div>
      </div>
      <ul class="contacts">
        <li class="contacts__item">
          <svg class="contacts__icon" viewBox="0 0 24 24" aria-hidden="true"><path d="M6.6 10.8c1.4 2.8 3.8 5.1 6.6 6.6l2.2-2.2c.3-.3.7-.4 1-.2 1.1.4 2.3.6 3.6.6.6 0 1 .4 1 1V20c0 .6-.4 1-1 1C10.6 21 3 13.4 3 4c0-.6.4-1 1-1h3.5c.6 0 1 .4 1 1 0 1.3.2 2.5.6 3.6.1.3 0 .7-.2 1z"/></svg>
          +12 123 456 7890
        </li>
        <li class="contacts__item">
          <svg class="contacts__icon" viewBox="0 0 24 24" aria-hidden="true"><path fill="none" stroke="#fff" stroke-width="2" d="M12 2a10 10 0 1 0 0 20 10 10 0 1 0 0-20zM2 12h20M12 2c3 3 3 17 0 20M12 2c-3 3-3 17 0 20M4 7h16M4 17h16"/></svg>
          Info@email.com
        </li>
        <li class="contacts__item">
          <svg class="contacts__icon" viewBox="0 0 24 24" aria-hidden="true"><path d="M12 2a7 7 0 0 0-7 7c0 5 7 13 7 13s7-8 7-13a7 7 0 0 0-7-7zm0 9.5A2.5 2.5 0 1 1 12 6.5a2.5 2.5 0 0 1 0 5z"/></svg>
          your street address
        </li>
      </ul>
    </div>
  </section>

</main>
</body>
</html>
```